Verdanix Medical Business Card

Create a high class Business card for Medical Aesthetics and Wellness Practice called Verdanix Medical Aesthetics and Wellness as per the logo attached.
Addresss is: 418 Harlan Brook Road Suite 312 Carrow Falls, New York 11093
Phone (555)204-7391 IG @verdanix_medical
Verdanixmedical.example

I need 5 different name configurations
1) Dr. Theo Valcourt
Aesthetics and Wellness Specialist
Medical Director

2) Rosalind Pettinger, NP
Clinical Nurse Manager

3) Marla Vostrik, RN
Aesthetic Nurse Specialist

4) Petra Halvesen, RN

5) Dana Kowbeck, L.E.
Senior Licensed Esthetician

Target Market(s)

22-55 Females

Industry/Entity Type

Medical Spa and Wellness

Contact Information for Business Card

Logo, address, phone, web, instagram, providers name

Requirements
Must have
• Attractive classy modern look

```html
<!DOCTYPE html>
<html lang="en">
<head>
<meta charset="utf-8">
<title>Verdanix Medical – Business Card</title>
<link rel="stylesheet" href="https://fonts.googleapis.com/css2?family=Cormorant+Garamond:wght@400&family=Cinzel:wght@400&family=Lato:wght@400;700&display=swap">
<style>
  :root {
    --backdrop: #9a9a9a;
    --teal-light: #1f7b8f;
    --teal-dark: #134b5c;
    --aqua: #6cc3c6;
    --ink-brand: #1d4f5e;
    --ink-name: #0f4a5c;
    --ink-body: #2a2a2a;
    --card-white: #ffffff;
    --icon: #5bbfc2;
  }
  * { margin: 0; padding: 0; box-sizing: border-box; }
  html, body { width: 1200px; height: 1000px; overflow: hidden; }
  body {
    position: relative;
    background: radial-gradient(ellipse at 50% 50%, #c9c9c9 0%, var(--backdrop) 80%);
    font-family: "Lato", sans-serif;
  }
  .card {
    position: absolute;
    left: 182px;
    width: 836px;
    height: 476px;
    border-radius: 20px;
    overflow: hidden;
    box-shadow: 0 2px 8px rgba(0,0,0,0.25);
  }
  .card-front {
    top: 17px;
    background: radial-gradient(ellipse at 8% 35%, var(--teal-light) 0%, var(--teal-dark) 55%);
  }
  .card-back { top: 507px; background: var(--card-white); }

  .wordmark {
    position: absolute;
    font-family: "Cormorant Garamond", serif;
    font-weight: 400;
    white-space: nowrap;
    transform: translateX(-50%);
    letter-spacing: 2px;
  }
  .tagline, .locale {
    position: absolute;
    font-family: "Cinzel", serif;
    white-space: nowrap;
    text-transform: uppercase;
    transform: translateX(-50%);
  }

  .card-front .wordmark { left: 418px; top: 170px; font-size: 66px; color: var(--aqua); }
  .card-front .tagline { left: 418px; top: 251px; font-size: 15.5px; color: var(--aqua); }
  .card-front .locale { left: 418px; top: 284px; font-size: 11px; letter-spacing: 6px; color: var(--aqua); }
  .figure-art {
    position: absolute; left: 43px; top: 261px; width: 100px; height: 184px;
    border-radius: 40px 40px 6px 6px;
    background: linear-gradient(180deg, rgba(108,195,198,0.22), rgba(108,195,198,0.08));
  }
  .ground-line {
    position: absolute; left: 31px; top: 445px; width: 775px; height: 1px;
    background: var(--aqua);
  }

  .card-back .wordmark { left: 231px; top: 137px; font-size: 42px; color: var(--ink-brand); }
  .card-back .tagline { left: 231px; top: 196px; font-size: 11px; color: var(--ink-brand); }
  .card-back .locale { left: 231px; top: 218px; font-size: 9px; letter-spacing: 4px; color: var(--ink-brand); }
  .provider-name {
    position: absolute; left: 231px; top: 264px; transform: translateX(-50%);
    white-space: nowrap; font-weight: 700; font-size: 33px; color: var(--ink-name);
  }
  .provider-role {
    position: absolute; left: 231px; top: 316px; transform: translateX(-50%);
    text-align: center; white-space: nowrap; font-size: 19px; line-height: 24px; color: var(--ink-body);
  }
  .provider-role strong { font-weight: 700; }

  .divider-shade {
    position: absolute; left: 452px; top: 115px; width: 70px; height: 345px;
    background: radial-gradient(ellipse at 0% 50%, rgba(0,0,0,0.16) 0%, rgba(0,0,0,0) 70%);
  }
  .social {
    position: absolute; right: 30px; top: 31px;
    display: flex; align-items: center; gap: 7px;
    font-size: 19px; color: #111;
  }
  .social-mark { width: 31px; height: 31px; border-radius: 6px; background: var(--icon); }
  .contact-icons { position: absolute; left: 566px; top: 175px; }
  .contact {
    position: absolute; left: 647px; top: 229px; transform: translateX(-50%);
    text-align: center; white-space: nowrap; font-size: 23px; color: var(--ink-body);
  }
  .contact p { line-height: 27px; }
  .contact .phone { margin-bottom: 16px; }
  .contact .web { margin-bottom: 16px; }
</style>
</head>
<body>
  <section class="card card-front">
    <div class="wordmark">Verdanix</div>
    <div class="tagline">Medical Aesthetics and Wellness</div>
    <div class="locale">New York</div>
    <div class="figure-art" role="img" aria-label="Single-line drawing of a woman with a measuring tape around her waist"></div>
    <div class="ground-line"></div>
  </section>

  <section class="card card-back">
    <div class="social"><span class="social-mark"></span>@verdanix_medical</div>

    <div class="wordmark">Verdanix</div>
    <div class="tagline">Medical Aesthetics and Wellness</div>
    <div class="locale">New York</div>
    <div class="provider-name">DR. THEO VALCOURT</div>
    <div class="provider-role">Aesthetics and Wellness Specialist<br><strong>Medical Director</strong></div>

    <div class="divider-shade"></div>

    <svg class="contact-icons" width="162" height="26" viewBox="0 0 162 26" fill="none" stroke="var(--icon)" stroke-width="1.6">
      <line x1="0" y1="13" x2="28" y2="13"/>
      <line x1="134" y1="13" x2="162" y2="13"/>
      <rect x="36" y="1" width="24" height="24" rx="4"/>
      <rect x="43" y="5" width="10" height="16" rx="2"/>
      <line x1="46.5" y1="18" x2="49.5" y2="18"/>
      <rect x="68" y="1" width="24" height="24" rx="4"/>
      <path d="M72 13 L88 6 L82 20 L79 15 Z"/>
      <line x1="79" y1="15" x2="88" y2="6"/>
      <rect x="100" y="1" width="24" height="24" rx="4"/>
      <path d="M112 21 C108 16 106 13 106 10.5 a6 6 0 0 1 12 0 C118 13 116 16 112 21 Z"/>
      <circle cx="112" cy="10.5" r="2"/>
    </svg>

    <div class="contact">
      <p class="phone">(555)204-7391</p>
      <p class="web">Verdanixmedical.example</p>
      <p>418 Harlan Brook Road</p>
      <p>Suite 312 Carrow Falls,</p>
      <p>New York 11093</p>
    </div>
  </section>
</body>
</html>
```